Security Consulting Firm needs brochure to be used for advertisement and sales

Need a brochure design for a new security consulting firm based in Metro Detroit called "K. Halvern Security Consulting, LLC" We provide consulting services related to safety and security for our clients. I have attached a file that contains excerpts from our business summary for info to be used (does not have to be word for work or exact), business contact info as well as statistics that i would like added somewhere. I also attached the company logo for use. I would like the logos for Pagemoot, CareerWeft and Snapvane somewhere on the brochure as well. Lastly , I would like the final design to communicate strength, safety, investigation and protection. Thank you
Target Market(s)
Corporate, schools, places of worship, large events, VIP
Industry/Entity Type
Business Consultant
Colors

```html
<!DOCTYPE html>
<html lang="en">
<head>
<meta charset="utf-8">
<title>K. Halvern Security Consulting – Brochure Covers</title>
<link href="https://fonts.googleapis.com/css2?family=Barlow:wght@400;500;700;800&display=swap" rel="stylesheet">
<style>
  :root {
    --backdrop: #dcdcdc;
    --paper: #ffffff;
    --brand-blue: #2a86c8;
    --deep-navy: #0e2f66;
    --photo-grey: #8a8a8a;
    --ink: #2b2b2b;
    --light-band: #d9d9d9;
  }
  * { box-sizing: border-box; margin: 0; padding: 0; }
  html, body { width: 1200px; height: 824px; overflow: hidden; }
  body {
    background: var(--backdrop);
    font-family: "Barlow", Arial, sans-serif;
    color: var(--ink);
  }
  .spread {
    position: absolute;
    left: 180px; top: 115px;
    width: 840px; height: 594px;
    display: flex;
    box-shadow: 0 10px 30px rgba(0,0,0,.18);
  }
  .page {
    position: relative;
    width: 420px; height: 594px;
    background: var(--paper);
    overflow: hidden;
  }
  .page-art { position: absolute; inset: 0; }
  .brand-name {
    font-weight: 800;
    font-size: 30px;
    letter-spacing: 1px;
    color: var(--deep-navy);
    line-height: 1;
    display: flex; align-items: center; gap: 8px;
  }
  .brand-name .mark-dot {
    width: 22px; height: 22px; border-radius: 50%;
    background: var(--brand-blue); flex: none;
  }
  .brand-sub {
    font-size: 9px; font-weight: 500; letter-spacing: 1.5px;
    text-transform: uppercase; color: var(--deep-navy);
    margin: 4px 0 0 30px;
  }
  .contact-list { list-style: none; font-size: 12px; font-weight: 500; }
  .contact-list li { display: flex; align-items: center; gap: 6px; line-height: 17px; }
  .contact-list svg { width: 11px; height: 11px; fill: var(--brand-blue); flex: none; }

  /* back cover */
  .back .brand-block { position: absolute; left: 110px; top: 62px; }
  .back .contact-list { position: absolute; left: 150px; top: 132px; }
  .follow {
    position: absolute; right: 18px; bottom: 28px; text-align: right;
  }
  .follow-title {
    font-size: 11px; font-weight: 700; color: var(--brand-blue);
    letter-spacing: .5px; margin-bottom: 5px;
  }
  .social-list { list-style: none; font-size: 10px; font-weight: 500; color: var(--brand-blue); }
  .social-list li { display: flex; align-items: center; justify-content: flex-end; gap: 5px; line-height: 15px; }
  .social-list li::before {
    content: ""; width: 9px; height: 9px; border-radius: 50%;
    border: 1.5px solid var(--brand-blue);
  }

  /* front cover */
  .cover-title {
    position: absolute; left: 34px; top: 232px; color: var(--paper);
    font-weight: 800; line-height: 1;
  }
  .cover-title .name { font-size: 44px; letter-spacing: 1px; }
  .cover-title .tagline {
    display: block;
    font-size: 19px; font-weight: 700; letter-spacing: 1px;
    margin: 6px 0 0 70px; line-height: 21px; text-transform: uppercase;
  }
  .front .contact-list { position: absolute; left: 30px; top: 478px; font-size: 11px; }
  .front .brand-block { position: absolute; right: 24px; top: 478px; }
  .front .brand-name { font-size: 24px; }
  .front .brand-sub { font-size: 7px; margin-left: 30px; }
</style>
</head>
<body>
<main class="spread">

  <section class="page back" aria-label="Back cover">
    <svg class="page-art" viewBox="0 0 420 594" preserveAspectRatio="none">
      <polygon points="0,292 420,178 420,188 0,302" fill="var(--light-band)"/>
      <polygon points="0,302 420,188 420,225 0,345" fill="var(--brand-blue)"/>
      <polygon points="0,345 420,225 420,400 110,594 0,594" fill="var(--photo-grey)"
               role="img" aria-label="Photo: technician on a ladder installing a security camera under a roof"/>
      <polygon points="90,594 420,392 420,404 116,594" fill="var(--brand-blue)"/>
    </svg>
    <div class="brand-block">
      <div class="brand-name"><span class="mark-dot"></span>K. HALVERN</div>
      <div class="brand-sub">Security Consulting, LLC</div>
    </div>
    <ul class="contact-list">
      <li><svg viewBox="0 0 24 24"><path d="M6.6 10.8a15 15 0 0 0 6.6 6.6l2.2-2.2a1 1 0 0 1 1-.25 11.4 11.4 0 0 0 3.6.6 1 1 0 0 1 1 1V20a1 1 0 0 1-1 1A17 17 0 0 1 3 4a1 1 0 0 1 1-1h3.5a1 1 0 0 1 1 1c0 1.250.2 2.45.6 3.6a1 1 0 0 1-.25 1z"/></svg>248-555-0147</li>
      <li><svg viewBox="0 0 24 24"><path d="M2 5h20v14H2zM4 7v.5l8 5 8-5V7l-8 5z"/></svg>info@khalvernsecurity.com</li>
      <li><svg viewBox="0 0 24 24"><circle cx="12" cy="12" r="10"/></svg>khalvernsecurity.com</li>
    </ul>
    <div class="follow">
      <p class="follow-title">FOLLOW US ON:</p>
      <ul class="social-list">
        <li>Pagemoot</li>
        <li>CareerWeft</li>
        <li>Snapvane</li>
      </ul>
    </div>
  </section>

  <section class="page front" aria-label="Front cover">
    <svg class="page-art" viewBox="0 0 420 594" preserveAspectRatio="none">
      <defs>
        <linearGradient id="cover-photo" x1="0" y1="0" x2="1" y2="1">
          <stop offset="0" stop-color="#1b3f86"/>
          <stop offset=".6" stop-color="#0e2f66"/>
          <stop offset="1" stop-color="#5a5a5a"/>
        </linearGradient>
      </defs>
      <polygon points="0,55 140,40 150,440 0,470" fill="var(--brand-blue)"/>
      <polygon points="40,0 420,0 420,390 170,430 110,300 40,90" fill="url(#cover-photo)"
               role="img" aria-label="Photo: hand holding a glowing digital globe with a padlock emblem"/>
      <polygon points="0,575 420,520 420,532 0,587" fill="var(--brand-blue)"/>
    </svg>
    <h1 class="cover-title">
      <span class="name">K. HALVERN</span>
      <span class="tagline">Security<br>Consulting<br>LLC</span>
    </h1>
    <ul class="contact-list">
      <li><svg viewBox="0 0 24 24"><path d="M6.6 10.8a15 15 0 0 0 6.6 6.6l2.2-2.2a1 1 0 0 1 1-.25 11.4 11.4 0 0 0 3.6.6 1 1 0 0 1 1 1V20a1 1 0 0 1-1 1A17 17 0 0 1 3 4a1 1 0 0 1 1-1h3.5a1 1 0 0 1 1 1c0 1.25.2 2.45.6 3.6a1 1 0 0 1-.25 1z"/></svg>248-555-0147</li>
      <li><svg viewBox="0 0 24 24"><path d="M2 5h20v14H2zM4 7v.5l8 5 8-5V7l-8 5z"/></svg>info@khalvernsecurity.com</li>
      <li><svg viewBox="0 0 24 24"><circle cx="12" cy="12" r="10"/></svg>khalvernsecurity.com</li>
    </ul>
    <div class="brand-block">
      <div class="brand-name"><span class="mark-dot"></span>K. HALVERN</div>
      <div class="brand-sub">Security Consulting, LLC</div>
    </div>
  </section>

</main>
</body>
</html>
```